Rack card for a integrative medical practice

Need an eye-catching rack card with our logo with content as provided. We have a membership based holistic medical practice which incorporates western and holistic medicine. We would like to focus on wellness and healthy lifestyle. See uploaded files for what is included in the membership. Would like 2 page rack card color on both sides. Logo must be on the front.

Target Market(s)

People looking for alternative medicine, healthy lifestyle.

Industry/Entity Type

Health and Wellness

Colors
00AB8E
00BBA5
67D7C9
C6EFE9
E9F9F6

Requirements
Must have
• Must spark interest at first sight. Clear message.
Nice to have
• Warm, bright and positive vibe. Organic, neutral and earthy colors.
Should not have
• Traditional medical practice vibe (cold, formal, industrial). No PINK except the logo.

```html
<!DOCTYPE html>
<html lang="en">
<head>
<meta charset="utf-8">
<title>Juniper Health &amp; Wellness – Rack Card</title>
<link href="https://fonts.googleapis.com/css2?family=Libre+Baskerville:wght@400;700&display=swap" rel="stylesheet">
<style>
  :root {
    --backdrop: #e4f3f9;
    --card: #f1f8fb;
    --ink: #2b2b2b;
    --ink-soft: #3a3a3a;
    --teal: #2aa8c0;
    --band: #b6e1ef;
    --band-pale: #d3eef6;
    --scene-a: #d6eef0;
    --scene-b: #f4b08a;
  }
  * { margin: 0; padding: 0; box-sizing: border-box; }
  html, body { width: 1200px; height: 1000px; overflow: hidden; }
  body {
    background: var(--backdrop);
    font-family: "Libre Baskerville", Georgia, serif;
    color: var(--ink);
    position: relative;
  }
  .rack-card {
    position: absolute;
    top: 108px;
    width: 360px;
    height: 784px;
    background: var(--card);
    overflow: hidden;
  }
  .rack-card--front { left: 183px; }
  .rack-card--back { left: 657px; }
  .decor { position: absolute; inset: 0; width: 360px; height: 784px; }

  /* Front */
  .brand {
    position: absolute; top: 30px; left: 0; width: 100%;
    text-align: center; color: var(--ink);
  }
  .brand__dot {
    display: block; width: 22px; height: 22px; border-radius: 50%;
    background: var(--teal); margin: 0 auto 10px;
  }
  .brand__name { font-size: 19px; font-weight: 400; letter-spacing: 0.5px; line-height: 1; }
  .brand__sub { font-size: 6px; letter-spacing: 0.6px; margin-top: 3px; }
  .hero-illustration {
    position: absolute; left: 22px; top: 117px; width: 316px; height: 230px;
    border-radius: 120px 140px 40px 60px;
    background: linear-gradient(135deg, var(--scene-a) 0%, #cfe9ee 60%, var(--scene-b) 130%);
  }
  .headline {
    position: absolute; top: 378px; left: 0; width: 100%; text-align: center;
  }
  .headline__title { font-size: 20.5px; font-weight: 700; line-height: 32px; letter-spacing: 1px; }
  .headline__name { font-size: 14px; letter-spacing: 1.2px; margin-top: 4px; }
  .tagline {
    position: absolute; top: 552px; left: 0; width: 100%; text-align: center;
    font-size: 9.8px; line-height: 18px; letter-spacing: 0.8px; text-transform: uppercase;
  }

  /* Back */
  .membership { position: absolute; top: 199px; left: 21px; right: 20px; }
  .membership__title { font-size: 18px; font-weight: 400; line-height: 32px; letter-spacing: 0.4px; margin-bottom: 20px; }
  .benefits { list-style: none; }
  .benefits li {
    position: relative; padding-left: 20px; font-size: 11.7px; line-height: 17px;
    margin-bottom: 16px;
  }
  .benefits li::before {
    content: ""; position: absolute; left: 0; top: 2px; width: 12px; height: 12px;
    background: var(--ink-soft);
  }
  .benefits li:nth-child(even)::before { background: var(--teal); }
  .benefits li:nth-child(7) { margin-bottom: 12px; }
  .location {
    position: absolute; top: 690px; left: 0; width: 100%; text-align: center;
    font-size: 11.5px; line-height: 18px;
  }
  .location__pin { display: block; margin: 0 auto 6px; }
  .location__city { font-weight: 700; }
</style>
</head>
<body>

<section class="rack-card rack-card--front">
  <svg class="decor" viewBox="0 0 360 784" aria-hidden="true">
    <polygon points="0,560 0,784 200,784" fill="var(--band)"/>
    <polygon points="0,500 0,520 240,784 220,784" fill="var(--band-pale)"/>
    <polygon points="0,620 0,700 84,784 0,784" fill="var(--band-pale)"/>
    <polygon points="48,640 78,610 78,660 48,690" fill="var(--teal)"/>
    <polygon points="60,740 72,728 72,750 60,762" fill="var(--teal)"/>
    <polygon points="0,760 22,784 0,784" fill="var(--teal)"/>
    <line x1="10" y1="505" x2="140" y2="640" stroke="var(--band)" stroke-width="1"/>
  </svg>

  <div class="brand">
    <span class="brand__dot"></span>
    <div class="brand__name">JUNIPER</div>
    <div class="brand__sub">HEALTH &amp; WELLNESS</div>
  </div>

  <div class="hero-illustration" role="img" aria-label="Illustration of a family seated in a clinic waiting room with a plant, pets and wall pictures"></div>

  <div class="headline">
    <h1 class="headline__title">INTEGRATIVE<br>MEDICAL PRACTICE</h1>
    <p class="headline__name">JUNIPER HEALTH &amp; WELLNESS</p>
  </div>

  <p class="tagline">A direct primary care practice<br>focused on a more holistice<br>and personal approach<br>to medicine.</p>
</section>

<section class="rack-card rack-card--back">
  <svg class="decor" viewBox="0 0 360 784" aria-hidden="true">
    <polygon points="165,0 360,0 360,192" fill="var(--band)"/>
    <polygon points="150,0 160,0 360,200 360,210" fill="var(--band-pale)"/>
    <polygon points="302,0 322,0 322,30 302,50" fill="var(--teal)"/>
    <polygon points="250,55 278,30 278,62 250,87" fill="var(--teal)"/>
    <polygon points="316,78 326,88 316,98" fill="var(--teal)"/>
    <polygon points="318,110 360,110 360,150" fill="var(--card)" opacity="0.7"/>
    <line x1="170" y1="10" x2="280" y2="170" stroke="var(--band)" stroke-width="1"/>
  </svg>

  <div class="membership">
    <h2 class="membership__title">WHAT’S INCLUDED IN YOUR<br>MEMBERSHIP:</h2>
    <ul class="benefits">
      <li>Unlimited office visits with no copay.</li>
      <li>Direct communication with your doctor.</li>
      <li>Discounted labs, imaging and medications.</li>
      <li>Free initial acupuncture session ($250 value).</li>
      <li>2 Composa testings per year ($100 value).</li>
      <li>Discounts for iv vitamin infusion therapy.</li>
      <li>Discounts for suplements and health products in the clinic.</li>
      <li>Personalized nutrition plan after advanced testing such as gut microbiome, hormonal, metabolism test, etc.</li>
    </ul>
  </div>

  <div class="location">
    <svg class="location__pin" width="22" height="36" viewBox="0 0 22 36" aria-hidden="true">
      <path d="M3 6 A11 11 0 0 1 19 6" fill="none" stroke="var(--teal)" stroke-width="3"/>
      <circle cx="11" cy="15" r="5" fill="var(--ink)"/>
      <polygon points="3,22 19,22 11,35" fill="var(--teal)"/>
    </svg>
    <div>1420 N ELM ST., STE 2B</div>
    <div class="location__city">Brookfield</div>
  </div>
</section>

</body>
</html>
```